New River III Precinct 6x11 GOTV postcard

We require BOTH persuasive copy and high-impact layout for an oversized 6x11 political mailer. This might be one person, but it likely requires a specialized "creative team." of an experienced political strategist copywriter PLUS a graphic designer - so the words fit the exact layout block, and the visuals reinforce the psychological punch of the headline.

The goal is to remove all excuses a targeted audience of ~900 registered Harvestline + ~1800 Unaffiliated voters in our precinct - have for not voting.

I need to be able to work by phone / online chat to iterate designs
I need to own the design in the top couple of software outputs that any printer service will require.

I want to experiment with very subtle background images as follows:
- Front of postcard that conveys "CHANGE" of not just seasons - but of encouraging change of precinct voter representation - so anything about fall foliage / conveyance of change tie-in is worthy of considering
- Back of postcard - any Appalachian long rage mountain view that includes 5-7 layers of hills in the distance.
Some photos as samples to consider.

Target Market(s)

~2,700 registered Harvestliners and Unaffiliated voters

Requirements
Must have
• We require BOTH persuasive copy and high-impact layout for an oversized 6x11 political mailer. This might be one person, but it likely requires a specialized "creative team." of an experienced political strategist copywriter PLUS a graphic designer - so the words fit the exact layout block, and the visuals reinforce the psychological punch of the headline
Nice to have
• subtle background photos

```html
<!DOCTYPE html>
<html lang="en">
<head>
<meta charset="utf-8">
<title>New River III Precinct GOTV Postcard</title>
<link href="https://fonts.googleapis.com/css2?family=Barlow+Condensed:ital,wght@0,300;1,300;1,800&family=Lato:wght@400;700;900&display=swap" rel="stylesheet">
<style>
  :root {
    --red: #e21d26;
    --navy: #2c2a6b;
    --white: #ffffff;
    --ink: #3a3a3a;
    --label: #555555;
    --stage-top: #7d7e82;
    --stage-bottom: #a4a5a8;
    --wood-dark: #3b2313;
    --wood-mid: #6a3f22;
    --leaf-red: #b8241a;
    --leaf-gold: #c9a92a;
  }
  * { margin: 0; padding: 0; box-sizing: border-box; }
  html, body { width: 1019px; height: 1200px; overflow: hidden; }
  body {
    background: linear-gradient(180deg, var(--stage-top), var(--stage-bottom));
    font-family: "Lato", sans-serif;
    position: relative;
  }
  .card {
    position: absolute;
    left: 88px;
    width: 843px;
    height: 460px;
    overflow: hidden;
    box-shadow: 0 2px 6px rgba(0,0,0,.25);
  }
  .card--front { top: 94px; }
  .card--back { top: 646px; background: var(--white); }

  /* FRONT */
  .front-photo {
    position: absolute; inset: 0;
    background:
      radial-gradient(circle at 8% 55%, rgba(184,36,26,.75) 0, rgba(184,36,26,0) 22%),
      radial-gradient(circle at 22% 92%, rgba(201,169,42,.6) 0, rgba(201,169,42,0) 14%),
      radial-gradient(circle at 98% 20%, rgba(200,110,30,.8) 0, rgba(200,110,30,0) 18%),
      radial-gradient(circle at 99% 55%, rgba(184,36,26,.9) 0, rgba(184,36,26,0) 16%),
      radial-gradient(circle at 97% 78%, rgba(201,169,42,.85) 0, rgba(201,169,42,0) 12%),
      linear-gradient(180deg, var(--wood-mid), var(--wood-dark) 60%, var(--wood-mid));
  }
  .headline {
    position: absolute; top: 29px; left: 0; height: 43px;
    display: flex; align-items: center;
  }
  .headline__tag {
    background: var(--red); color: var(--white);
    height: 43px; width: 174px;
    display: flex; align-items: center; justify-content: center;
    font-family: "Barlow Condensed", sans-serif; font-weight: 300; font-style: italic;
    font-size: 42px; letter-spacing: 1px;
    clip-path: polygon(0 0, 100% 0, 97% 100%, 0 100%);
  }
  .headline__main {
    color: var(--white);
    font-family: "Barlow Condensed", sans-serif; font-weight: 800; font-style: italic;
    font-size: 42px; margin-left: 9px; letter-spacing: .3px;
  }
  .headline__flag {
    position: absolute; left: 530px; top: 36px; width: 276px; height: 29px;
    background: linear-gradient(90deg, #3a3778 0%, #8a6a8a 40%, #e6b4b6 70%, #d9545a 100%);
    transform: skewX(-8deg);
  }

  .issues { position: absolute; top: 85px; color: var(--white); font-size: 10.6px; line-height: 11.7px; }
  .issues--left { left: 41px; width: 192px; }
  .issues--mid { left: 270px; width: 262px; }
  .issue { margin-bottom: 10px; }
  .issue__title {
    display: inline-block; background: var(--red);
    font-weight: 900; font-size: 14.5px; line-height: 16px;
    padding: 0 6px 0 0; margin-bottom: 2px;
  }
  .issue__lead { font-weight: 700; font-style: italic; }
  .issue__call { font-weight: 700; }

  .ballot {
    position: absolute; left: 556px; top: 77px; width: 250px; height: 383px;
    background: var(--white); padding: 16px 13px;
  }
  .ballot__star { position: absolute; right: 6px; top: 18px; }
  .ballot__title {
    position: relative; color: var(--red); font-weight: 900;
    font-size: 12.4px; line-height: 11.6px; margin-bottom: 13px;
  }
  .race { position: relative; margin-bottom: 12px; }
  .race__office { color: var(--label); font-size: 11.3px; line-height: 12px; }
  .race__name { color: var(--navy); font-weight: 900; font-size: 12.8px; line-height: 13px; }
  .race--measure .race__name { color: var(--red); font-size: 12.4px; line-height: 13.3px; }
  .ballot-edge {
    position: absolute; left: 806px; top: 77px; width: 37px; height: 383px;
    background: linear-gradient(180deg, #c86e1e, var(--leaf-red) 45%, var(--leaf-gold) 75%, var(--leaf-red));
  }

  /* BACK */
  .mountain-photo {
    position: absolute; left: 0; top: 215px; width: 843px; height: 245px;
    background: linear-gradient(180deg, rgba(255,255,255,0) 0%, #c3ccd2 14%, #8fa79c 35%, #5f8450 60%, #4d7a2c 100%);
    -webkit-mask-image: linear-gradient(90deg, #000 55%, transparent 80%);
    mask-image: linear-gradient(90deg, #000 55%, transparent 80%);
  }
  .letter { position: absolute; left: 19px; top: 18px; width: 400px; color: var(--ink); }
  .letter__greeting {
    color: var(--red);
    font-family: "Barlow Condensed", sans-serif; font-weight: 800; font-style: italic;
    font-size: 32px; line-height: 36px; margin-bottom: 8px;
  }
  .letter p { font-size: 10.8px; line-height: 12.7px; margin-bottom: 6.4px; }
  .letter strong { font-weight: 900; }

  .rally {
    position: absolute; left: 0; top: 242px; width: 390px; height: 41px;
    background: var(--navy); color: var(--white);
    padding: 6px 19px; font-size: 12.8px; line-height: 15px;
  }
  .rally strong { font-weight: 900; }
  .rally__star { position: absolute; left: 378px; top: 236px; }

  .checklist { position: absolute; left: 19px; top: 302px; list-style: none; }
  .checklist li {
    display: flex; align-items: center; gap: 8px;
    color: var(--white); font-weight: 900; font-size: 12.6px; line-height: 19.1px;
    text-shadow: 0 1px 2px rgba(0,0,0,.35);
  }
</style>
</head>
<body>

<section class="card card--front" aria-label="Postcard front">
  <div class="front-photo" role="img" aria-label="Dark wood background framed by red, orange and gold autumn leaves"></div>

  <header class="headline">
    <div class="headline__tag">VOTE FOR</div>
    <h1 class="headline__main">NEW REPRESENTATION</h1>
  </header>
  <div class="headline__flag" role="img" aria-label="Waving national flag banner"></div>

  <div class="issues issues--left">
    <div class="issue">
      <div class="issue__title">LOCAL PAIN</div>
      <p><span class="issue__lead">Thanks to current representatives</span> — and sadly, to avoid accountability, they’ve cleverly delayed many / most impacts until AFTER the 2026 election.<br><span class="issue__call">VOTE FOR CHANGE</span></p>
    </div>
    <div class="issue">
      <div class="issue__title">FAMILY BUDGET</div>
      <p>Exploded costs for everything: groceries, gas, car insurance, rent.</p>
    </div>
    <div class="issue">
      <div class="issue__title">HEALTH</div>
      <p>Expired subsidies, tax credits mean ~1m in NC will lose coverage or pay more. 50% cuts to Hospitals, Mental Health facilities, rural facilities will be closing.</p>
    </div>
    <div class="issue">
      <div class="issue__title">REPRODUCTIVE RIGHTS</div>
      <p>Government authoritarian intrusion<br>— censure women’s rights.</p>
    </div>
    <div class="issue">
      <div class="issue__title">FOOD SECURITY</div>
      <p>Weaponized Hunger — cuts to SNAP; school meals cut; add’l work reqmts.</p>
    </div>
  </div>

  <div class="issues issues--mid">
    <div class="issue">
      <div class="issue__title">EDUCATION</div>
      <p>Watauga $2.2mm shortfall personnel cuts, freezes in hiring, teacher training. Abandoning civil rights of Special Ed students to HHS and DOJ.</p>
    </div>
    <div class="issue">
      <div class="issue__title">HOUSING</div>
      <p>~25% of renters are spending over 50% of income on rent. Especially bad locally; predatory leasing terms and skyrocketing rents. Proposed legislation is transforming HUD with the goal of getting rid of Section 8 housing that cares for vulnerable populations.</p>
    </div>
    <div class="issue">
      <div class="issue__title">ENERGY</div>
      <p>In 2022 Boone achieved 100% renewable energy in town buildings; this is now being destroyed by repeal of renewable energy project funding. Ridge State Innovation District prepares renewable workforce technologies — all this is now in limbo.</p>
    </div>
    <div class="issue">
      <div class="issue__title">ENVIRONMENT</div>
      <p>Reduced protections from coal ash pond leaks threaten public health. Corporations not held responsible for damage; public picks up the tab. Environmental justice enforcement no longer a priority. Logging in Watauga with no public oversight. It’s the “haz-mat” model do nothing, wait for catastrophe, then fix it.</p>
    </div>
  </div>

  <aside class="ballot">
    <svg class="ballot__star" width="90" height="86" viewBox="0 0 100 95" aria-hidden="true">
      <polygon points="50,0 61,35 98,35 68,57 79,93 50,71 21,93 32,57 2,35 39,35" fill="#eeeeef"/>
    </svg>
    <h2 class="ballot__title">SAMPLE BALLOT<br>RECOMMENDATIONS</h2>
    <div class="race"><div class="race__office">US SENATE</div><div class="race__name">RAY COLTON</div></div>
    <div class="race"><div class="race__office">US HOUSE – DISTRICT 5</div><div class="race__name">CHET HOLLIS</div></div>
    <div class="race race--measure"><div class="race__name">REQMT TO SHOW ID FOR VOTERS<br>NOT IN PERSON-NO</div></div>
    <div class="race"><div class="race__office">STATE SENATE DISTRICT 47</div><div class="race__name">FRED HASKINS</div></div>
    <div class="race"><div class="race__office">HOUSE OF REP’S DISTRICT 93</div><div class="race__name">CARL WHITMAN</div></div>
    <div class="race"><div class="race__office">NC SUPREME COURT</div><div class="race__name">ALMA ELLIS</div></div>
    <div class="race"><div class="race__office">NC COURT OF APPEALS – SEAT 1</div><div class="race__name">JOEL ASHFORD</div></div>
    <div class="race"><div class="race__office">NC COURT OF APPEALS – SEAT 2</div><div class="race__name">TROY HANLEY</div></div>
    <div class="race"><div class="race__office">NC COURT OF APPEALS – SEAT 3</div><div class="race__name">CLARA WOZNIAK</div></div>
  </aside>
  <div class="ballot-edge" role="img" aria-label="Autumn maple leaves along the right edge"></div>
</section>

<section class="card card--back" aria-label="Postcard back">
  <div class="mountain-photo" role="img" aria-label="Layered Appalachian mountain ridges fading into green forest"></div>

  <article class="letter">
    <h2 class="letter__greeting">Dear New River III Neighbor.</h2>
    <p>We live in a representative democracy. We expect our representatives will exercise independent thinking and support policies and legislation that don’t harm us — and that reflect the <strong>MAJORITY VIEWS</strong> of precinct citizens.</p>
    <p>But our current representatives <strong>HAVE STOPPED LISTENING</strong> — they are now bringing harmful policies straight to Watauga County. I<strong>T’S TIME TO HOLD THEM ACCOUNTABLE AND VOTE THEM OUT.</strong></p>
    <p>Make no mistake: in 2026, every election is partisan. Even Judicial seats are now tied directly to state platforms.</p>
    <p>Any candidate who refuses to publicly condemn Raleigh’s gerrymandered overreach into Watauga politics — or refuses to fight funding cuts for our healthcare, education, and environmental justice — is actively supporting these harmful policies.</p>
  </article>

  <div class="rally">They are hoping their silence fools you. <strong>DON’T BE FOOLED.</strong><br>This November, <strong>VOTE FOR CHANGE.</strong></div>
  <svg class="rally__star" width="50" height="48" viewBox="0 0 100 95" aria-hidden="true">
    <polygon points="50,0 61,35 98,35 68,57 79,93 50,71 21,93 32,57 2,35 39,35" fill="#e21d26"/>
  </svg>

  <ul class="checklist">
    <li><svg width="15" height="15" viewBox="0 0 16 16" aria-hidden="true"><circle cx="8" cy="8" r="6.8" fill="none" stroke="#fff" stroke-width="1.6"/><path d="M4.5 8.2l2.4 2.4 4.8-5" fill="none" stroke="#fff" stroke-width="2"/></svg>YOU ARE A REGISTERED VOTER IN WATAUGA COUNTY</li>
    <li><svg width="15" height="15" viewBox="0 0 16 16" aria-hidden="true"><circle cx="8" cy="8" r="6.8" fill="none" stroke="#fff" stroke-width="1.6"/><path d="M4.5 8.2l2.4 2.4 4.8-5" fill="none" stroke="#fff" stroke-width="2"/></svg>YOU RESIDE IN PRECINCT: NEW RIVER III</li>
    <li><svg width="15" height="15" viewBox="0 0 16 16" aria-hidden="true"><circle cx="8" cy="8" r="6.8" fill="none" stroke="#fff" stroke-width="1.6"/><path d="M4.5 8.2l2.4 2.4 4.8-5" fill="none" stroke="#fff" stroke-width="2"/></svg>POLLING PLACES AVAILABLE TO YOU ARE: LOCATION., 2, 3</li>
    <li><svg width="15" height="15" viewBox="0 0 16 16" aria-hidden="true"><circle cx="8" cy="8" r="6.8" fill="none" stroke="#fff" stroke-width="1.6"/><path d="M4.5 8.2l2.4 2.4 4.8-5" fill="none" stroke="#fff" stroke-width="2"/></svg>EARLY VOTING STARTS ON:</li>
    <li><svg width="15" height="15" viewBox="0 0 16 16" aria-hidden="true"><circle cx="8" cy="8" r="6.8" fill="none" stroke="#fff" stroke-width="1.6"/><path d="M4.5 8.2l2.4 2.4 4.8-5" fill="none" stroke="#fff" stroke-width="2"/></svg>DEADLINE TO APPLY FOR MAIL-IN BALLOTS</li>
    <li><svg width="15" height="15" viewBox="0 0 16 16" aria-hidden="true"><circle cx="8" cy="8" r="6.8" fill="none" stroke="#fff" stroke-width="1.6"/><path d="M4.5 8.2l2.4 2.4 4.8-5" fill="none" stroke="#fff" stroke-width="2"/></svg>KNOW THE RULES TO ENSURE YOUR MAIL-IN-BALLOT COUNTS</li>
  </ul>
</section>

</body>
</html>
```